Business cards for Remote DBA team

Business cards for team offering database administration, consultation, machine learning and AI services. As of now team is using both
www.korvilnet.cz and www.brestmoorlab.cz URLs

Target Market(s)

IT managers

Industry/Entity Type

It Professional

Contact Information for Business Card

Should include logo
name, email, phone, twitter tag

Font styles to use
Sans Serif

Colors

Designer to choose colors to be used in the design.

```html
<!DOCTYPE html>
<html lang="en">
<head>
<meta charset="utf-8">
<title>Korvil Data Lab – Business Cards</title>
<link rel="stylesheet" href="https://fonts.googleapis.com/css2?family=Montserrat:wght@800&family=Arimo:wght@400;700&display=swap">
<style>
  :root {
    --backdrop: #2a2a2c;
    --brand-blue: #1a8bc6;
    --brand-blue-dark: #1579ae;
    --paper: #ffffff;
    --ink-grey: #6d6e70;
    --rule-blue: #4aa3d4;
  }
  * { box-sizing: border-box; margin: 0; padding: 0; }
  html, body {
    width: 1200px; height: 880px; overflow: hidden;
    background: var(--backdrop);
    font-family: "Arimo", Arial, sans-serif;
  }
  .sheet {
    width: 1200px; height: 880px;
    display: flex; flex-direction: column;
    align-items: center; justify-content: center; gap: 30px;
  }
  .card {
    position: relative;
    width: 700px; height: 400px;
    border-radius: 26px;
    overflow: hidden;
    box-shadow: 0 10px 24px rgba(0,0,0,0.45);
  }
  /* Front */
  .card--front { background: var(--brand-blue); }
  .pattern-area {
    position: absolute; right: 0; top: 0;
    width: 440px; height: 300px;
    background: radial-gradient(ellipse at 55% 45%, rgba(255,255,255,0.14), rgba(255,255,255,0) 70%);
  }
  .wordmark {
    position: absolute;
    display: flex; align-items: center; gap: 14px;
  }
  .wordmark__dot {
    width: 16px; height: 16px; border-radius: 50%;
    flex: none;
  }
  .wordmark__name {
    font-family: "Montserrat", Arial, sans-serif;
    font-weight: 800;
    line-height: 0.98;
    text-transform: uppercase;
    letter-spacing: 0.5px;
  }
  .card--front .wordmark { left: 110px; top: 200px; }
  .card--front .wordmark__dot { background: var(--paper); }
  .card--front .wordmark__name { color: var(--paper); font-size: 38px; }

  /* Back */
  .card--back { background: var(--paper); }
  .card--back .wordmark { left: 120px; top: 150px; }
  .card--back .wordmark__dot { background: var(--brand-blue); }
  .card--back .wordmark__name { color: var(--brand-blue); font-size: 34px; }
  .divider {
    position: absolute; left: 378px; top: 60px;
    width: 1.5px; height: 190px;
    background: var(--rule-blue);
  }
  .contact {
    position: absolute; left: 408px; top: 58px;
    color: var(--ink-grey); font-size: 14.5px; line-height: 1.35;
  }
  .contact__name {
    color: var(--brand-blue); font-weight: 700; font-size: 23px; line-height: 1.1;
  }
  .contact__role { font-size: 14px; margin-bottom: 12px; }
  .contact__address { margin-bottom: 10px; }
  .contact__line { display: flex; align-items: center; gap: 8px; }
  .contact__icon { width: 13px; height: 13px; flex: none; fill: var(--brand-blue); }
  .url-band {
    position: absolute; left: 0; right: 0; bottom: 30px; height: 62px;
    background: var(--brand-blue);
    display: flex; align-items: center; justify-content: center; gap: 18px;
    color: var(--paper); font-size: 16px; letter-spacing: 3px;
  }
  .url-band__sep { opacity: 0.9; }
</style>
</head>
<body>
<main class="sheet">
  <section class="card card--front" aria-label="Card front">
    <div class="pattern-area" role="img" aria-label="Faint hexagon pattern with data and analytics icons"></div>
    <div class="wordmark">
      <span class="wordmark__dot"></span>
      <span class="wordmark__name">Korvil<br>Data<br>Lab</span>
    </div>
  </section>

  <section class="card card--back" aria-label="Card back">
    <div class="wordmark">
      <span class="wordmark__dot"></span>
      <span class="wordmark__name">Korvil<br>Data<br>Lab</span>
    </div>
    <div class="divider"></div>
    <div class="contact">
      <p class="contact__name">Tomas Veller</p>
      <p class="contact__role">Director</p>
      <p class="contact__address">PO Box 418, Harlow Lane 7<br>Brestmoor Quarter</p>
      <p class="contact__line">
        <svg class="contact__icon" viewBox="0 0 16 16" aria-hidden="true"><path d="M3.6 1.2l2.4 2.6-1.4 2c.9 1.9 2.5 3.6 4.5 4.6l2-1.4 2.6 2.4-1.4 2.4C6.6 13.6 2.4 9.4 1.2 3z"/></svg>
        (555) 014 2263
      </p>
      <p class="contact__line">
        <svg class="contact__icon" viewBox="0 0 16 16" aria-hidden="true"><path d="M1 3h14v10H1z M2 4.2v.4l6 4 6-4v-.4z" fill-rule="evenodd"/></svg>
        hello@korvilnet.cz
      </p>
      <p class="contact__line">
        <svg class="contact__icon" viewBox="0 0 16 16" aria-hidden="true"><circle cx="8" cy="8" r="6.5"/></svg>
        @korvildatalab
      </p>
    </div>
    <div class="url-band">
      <span>www.korvilnet.cz</span>
      <span class="url-band__sep">|</span>
      <span>www.brestmoorlab.cz</span>
    </div>
  </section>
</main>
</body>
</html>
```